Marketing Company Needs Creative Brochure Design

We need a brochure design for a new company based in the Twin Cities called 'Lanternway Marketing'. We work with our clients to get them found on the internet and at the top of Zorvex page rankings. We offer a variety of marketing tools for our clients from Search Engine Optimization (SEO), to social media, videos, blogs, article marketing, etc... We would like to incorporate the blacksmith theme. Our colors are red and black. The final design should communicate business growth.

Target Market(s)

business owners

Industry/Entity Type

Marketing

Requirements
Should not have
• Although we would like to incorporate the blacksmith theme, please don't make it cheesy. Think sophistication and creativity.

```html
<!DOCTYPE html>
<html lang="en">
<head>
<meta charset="utf-8">
<title>Lanternway Marketing – Web Presence</title>
<link rel="stylesheet" href="https://fonts.googleapis.com/css2?family=Bebas+Neue&family=Alegreya+Sans:wght@400;700&display=swap">
<style>
  :root {
    --canvas: #000000;
    --red-deep: #c8151b;
    --red-mid: #e0261c;
    --orange-glow: #f0561e;
    --band: rgba(150, 10, 18, 0.55);
    --ink: #0c0c0c;
    --paper: #ffffff;
    --tab: #1d1f24;
    --photo-light: #d9c3a0;
    --photo-dark: #3a3d45;
  }
  * { margin: 0; padding: 0; box-sizing: border-box; }
  html, body { width: 1200px; height: 900px; overflow: hidden; background: var(--canvas); }
  .spread { position: absolute; left: 30px; top: 167px; width: 1136px; height: 568px; }
  .panel-red {
    position: absolute; left: 0; top: 0; width: 568px; height: 568px;
    background: radial-gradient(ellipse 70% 60% at 45% 60%, var(--orange-glow) 0%, var(--red-mid) 45%, var(--red-deep) 100%);
    overflow: hidden;
  }
  .side-tab {
    position: absolute; left: 0; top: 448px; width: 18px; height: 88px;
    background: var(--tab); border-radius: 0 6px 6px 0;
  }
  .section-title {
    position: absolute; left: 49px; top: 30px;
    font-family: "Bebas Neue", sans-serif; font-size: 84px; line-height: 84px;
    color: var(--ink); letter-spacing: 0.5px;
  }
  .play-icon { position: absolute; left: 425px; top: 42px; }
  .quote-band {
    position: absolute; left: 49px; top: 108px; width: 519px; height: 76px;
    background: var(--band); border-radius: 8px 0 0 8px;
  }
  .quote-band p {
    position: absolute; left: 13px; top: 8px;
    font-family: "Bebas Neue", sans-serif; font-size: 32px; line-height: 32px;
    color: var(--paper);
  }
  .body-copy {
    position: absolute; left: 49px; top: 205px; width: 470px;
    font-family: "Alegreya Sans", sans-serif; font-size: 12.2px; line-height: 15.7px;
    color: var(--paper);
  }
  .body-copy p + p { margin-top: 15px; }
  .strategies { position: absolute; left: 49px; top: 420px; font-family: "Alegreya Sans", sans-serif; color: var(--paper); }
  .strategies h3 { font-size: 12px; font-weight: 700; letter-spacing: 0.3px; margin-bottom: 4px; }
  .strategies ul { list-style: none; }
  .strategies li { font-size: 12.2px; line-height: 19.8px; position: relative; padding-left: 8px; }
  .strategies li::before {
    content: ""; position: absolute; left: 0; top: 7px;
    border-left: 5px solid var(--ink); border-top: 3px solid transparent; border-bottom: 3px solid transparent;
  }
  .photo-team {
    position: absolute; left: 569px; top: 0; width: 567px; height: 568px;
    background: linear-gradient(180deg, var(--photo-light) 0%, #b9a78c 45%, var(--photo-dark) 100%);
  }
  .photo-marker { position: absolute; left: 580px; top: 480px; }
</style>
</head>
<body>
  <main class="spread">
    <section class="panel-red">
      <div class="side-tab"></div>
      <h1 class="section-title">Web Presence</h1>
      <svg class="play-icon" width="28" height="28" viewBox="0 0 28 28" aria-hidden="true">
        <circle cx="14" cy="14" r="13" fill="#a80f16"/>
        <circle cx="14" cy="14" r="9" fill="#5a0a0e"/>
        <path d="M11 9.5 L18 14 L11 18.5 Z" fill="#e8e8e8"/>
      </svg>
      <div class="quote-band">
        <p>“We use the best and most relevant<br>keywords for your business”</p>
      </div>
      <div class="body-copy">
        <p>Your company is a little fish in a big pond on the World Wide Web. Let us highlight your company and bring it to the surface. Our team is highly knowledgeable in Search Engine Optimization, or the craft of getting you listed high and on the front page of search results so that potential clients can find you. We use the best and most relevant keywords for your business, and we create a plan to optimize your site for these keywords. Search Engine Optimization is constantly evolving, and we are always working to stay ahead of the trends to provide the best service to our clients. When you appear higher in search results, a larger volume of people will visit your site and discover your business – it’s as simple as that.</p>
        <p>Your website is a powerful tool used to communicate with potential clients. Make sure you are sending the right message at first click!We can professionally design custom websites full of engaging content and an intuitive navigation system that captures leads by offering incentives to potential clients. We can also work with you to optimize your current site to ensure that your site is search engine-friendly.</p>
      </div>
      <div class="strategies">
        <h3>STRATEGIES</h3>
        <ul>
          <li>Conduct Thorough Keyword Research</li>
          <li>Acquire Strategic Domain Name</li>
          <li>Build Organic Search Results</li>
          <li>Create Key Online Directories Profiles</li>
          <li>Pay Per Click Campaign Management</li>
        </ul>
      </div>
    </section>
    <div class="photo-team" role="img" aria-label="Photo of four business people in suits gathered around a laptop at a desk, smiling at the screen"></div>
    <svg class="photo-marker" width="8" height="6" viewBox="0 0 8 6" aria-hidden="true"><path d="M0 0 H8 L4 6 Z" fill="#ffffff"/></svg>
  </main>
</body>
</html>
```